Vok Social Network Needs Web Front

Vok needs a web front end to describe its vision, put out blog articles for our new California startup. Vok is a Social Network and Social Media Application which starts with the idea that we all do good things. Take for instance yourself, while many may call you a graphic artists and design genius, at your core, what you enjoy about what you do is “creating opportunity” for ideas and businesses to excel.

We want to first appeal to every day people - college students, parents, retail professionals but be attractive to volunteers, philanthropists and spiritual organizations.

Instead of limiting colors and design style, I will provide our logo and our mobile profile screen. Please take this as inspiration (feel free not to let our existing style limit yours).

The final design should communicate social network/mobile/software genius.

Industry/Entity Type

Media

```html
<!DOCTYPE html>
<html lang="en">
<head>
<meta charset="utf-8">
<title>Vok — Social Network &amp; Social Media Application</title>
<link href="https://fonts.googleapis.com/css2?family=Open+Sans:wght@300;400;600;700&display=swap" rel="stylesheet">
<style>
:root{
  --red:#f0333a;
  --ink:#2b2b2b;
  --muted:#8a8a8a;
  --line:#e4e4e4;
  --paper:#ffffff;
  --band:#f1f1f1;
  --footer:#2a2a2a;
  --footer-deep:#1f1f1f;
  --hero-a:#b7a79a;
  --hero-b:#d9cfc4;
  --hero-c:#8c8f98;
}
*{box-sizing:border-box;margin:0;padding:0}
html,body{width:788px;height:1200px;overflow:hidden}
body{font-family:"Open Sans",Arial,sans-serif;color:var(--ink);background:var(--paper);position:relative}

/* Hero */
.hero{position:absolute;left:0;top:0;width:788px;height:420px;overflow:hidden}
.hero-photo{position:absolute;inset:0;background:
  radial-gradient(circle at 25% 55%,#6d7078 0,transparent 38%),
  radial-gradient(circle at 80% 30%,var(--hero-b) 0,transparent 45%),
  linear-gradient(120deg,var(--hero-c),var(--hero-a) 45%,var(--hero-b))}
.brand{position:absolute;left:16px;top:0;width:62px;height:62px;background:#111;color:#fff;
  font-weight:700;font-size:24px;display:flex;align-items:center;justify-content:center}
.account{position:absolute;right:18px;top:8px;display:flex;gap:4px}
.account a{font-size:9px;color:#fff;text-decoration:none;padding:3px 9px;background:var(--red)}
.account a.login{background:#222}
.hero-copy{position:absolute;left:390px;top:138px;width:340px;color:#fff}
.hero-copy h1{font-weight:300;font-size:27px;line-height:32px}
.hero-copy p{margin-top:12px;font-size:9.5px;line-height:15px;opacity:.9}
.store-dots{display:flex;gap:10px;margin-top:14px}
.store-dots span{width:16px;height:16px;border-radius:50%;background:rgba(255,255,255,.85)}
.slider-nav{position:absolute;right:18px;top:366px;display:flex;gap:4px}
.slider-nav span{width:18px;height:18px;background:rgba(0,0,0,.55);display:flex;align-items:center;justify-content:center}

/* Features */
.features{position:absolute;top:420px;left:0;width:788px;height:170px;display:flex;justify-content:center;gap:40px;padding-top:22px}
.feature{width:200px;text-align:center}
.feature svg{display:block;margin:0 auto 8px}
.feature h3{font-weight:400;font-size:16px}
.feature p{font-size:8.5px;line-height:13px;color:var(--muted);margin-top:6px}

.divider{position:absolute;top:648px;left:0;width:788px;height:1px;background:var(--line)}
.divider-nav{position:absolute;top:640px;left:370px;display:flex;gap:6px}
.divider-nav span{width:18px;height:18px;border:1px solid var(--line);border-radius:50%;background:#fff;display:flex;align-items:center;justify-content:center}

/* Blog */
.blog-title{position:absolute;top:676px;width:788px;text-align:center;font-weight:400;font-size:21px}
.posts{position:absolute;top:730px;left:58px;display:flex;gap:18px}
.post{width:154px;height:178px;background:#fff;border:1px solid var(--line);border-radius:6px;overflow:hidden;text-align:center}
.post-photo{height:100px}
.post h4{font-size:9px;font-weight:600;margin-top:8px}
.post time{display:block;font-size:7px;color:var(--muted);margin-top:2px}
.post p{font-size:7px;line-height:10px;color:var(--muted);padding:4px 12px 0}
.post .more{display:inline-block;margin-top:6px;font-size:7px;color:var(--ink);border:1px solid #cfcfcf;border-radius:9px;padding:2px 9px}

/* Newsletter */
.newsletter{position:absolute;top:918px;left:0;width:788px;height:118px;background:var(--band);text-align:center}
.newsletter h2{display:flex;justify-content:center;align-items:center;gap:10px;font-weight:300;font-size:21px;color:#555;margin-top:20px}
.signup{display:flex;justify-content:center;margin-top:16px}
.signup .field{width:356px;height:30px;background:#fff;border:1px solid #ddd;border-radius:15px 0 0 15px;font-size:8px;color:#aaa;text-align:left;padding:9px 18px}
.signup .submit{width:90px;height:30px;margin-left:-14px;background:var(--red);color:#fff;font-size:10px;font-weight:700;border-radius:15px;display:flex;align-items:center;justify-content:center}

/* Footer */
.footer{position:absolute;top:1042px;left:0;width:788px;height:158px;background:var(--footer);text-align:center;color:#bbb}
.footer h5{font-weight:400;font-size:11px;margin-top:22px;color:#ddd}
.socials{display:flex;justify-content:center;gap:10px;margin-top:14px}
.socials span{width:22px;height:22px;border-radius:50%;background:#4a4a4a}
.legal{position:absolute;bottom:0;left:0;width:788px;height:46px;background:var(--footer-deep);font-size:7.5px;color:#888;padding-top:18px}
</style>
</head>
<body>

<header class="hero">
  <div class="hero-photo" role="img" aria-label="Blurred street scene with a hand holding a smartphone showing app icons"></div>
  <div class="brand">Vok</div>
  <nav class="account"><a href="#">Sign Up</a><a href="#" class="login">Login</a></nav>
  <div class="hero-copy">
    <h1>Social Network &amp;<br>Social Media Application</h1>
    <p>Share the good things you do every day, connect with people who care and build a kinder network around your ideas.</p>
    <div class="store-dots"><span></span><span></span><span></span></div>
  </div>
  <div class="slider-nav">
    <span><svg width="8" height="8" viewBox="0 0 8 8"><path d="M5.5 1 2.5 4l3 3" fill="none" stroke="#fff" stroke-width="1.3"/></svg></span>
    <span><svg width="8" height="8" viewBox="0 0 8 8"><path d="M2.5 1l3 3-3 3" fill="none" stroke="#fff" stroke-width="1.3"/></svg></span>
  </div>
</header>

<section class="features">
  <div class="feature">
    <svg width="30" height="24" viewBox="0 0 30 24" fill="var(--red)"><circle cx="15" cy="7" r="5"/><path d="M5 23c0-6 4-9 10-9s10 3 10 9z"/><circle cx="5" cy="9" r="3.5"/><circle cx="25" cy="9" r="3.5"/><path d="M0 21c0-4 2-6 5-6 1.5 0 2.4.4 3 1-1.6 1.4-2.4 3-2.6 5z"/><path d="M30 21c0-4-2-6-5-6-1.5 0-2.4.4-3 1 1.6 1.4 2.4 3 2.6 5z"/></svg>
    <h3>User Friendly</h3>
    <p>Clean screens and simple steps help anyone join, share and connect within minutes.</p>
  </div>
  <div class="feature">
    <svg width="26" height="24" viewBox="0 0 26 24"><path fill="var(--red)" d="M13 23 2.5 12.5A6.5 6.5 0 0 1 13 4a6.5 6.5 0 0 1 10.5 8.5z"/></svg>
    <h3>Designed with love</h3>
    <p>Every detail is crafted to make giving, helping and sharing feel natural.</p>
  </div>
  <div class="feature">
    <svg width="26" height="24" viewBox="0 0 26 24" fill="var(--red)"><path d="M10 1h6v9h5l-8 8-8-8h5z"/><path d="M2 17h3v4h16v-4h3v7H2z"/></svg>
    <h3>Easy Install</h3>
    <p>Download the app, create a profile and start sharing good deeds today.</p>
  </div>
</section>

<div class="divider"></div>
<div class="divider-nav">
  <span><svg width="7" height="7" viewBox="0 0 8 8"><path d="M5.5 1 2.5 4l3 3" fill="none" stroke="#999" stroke-width="1.2"/></svg></span>
  <span><svg width="7" height="7" viewBox="0 0 8 8"><path d="M2.5 1l3 3-3 3" fill="none" stroke="#999" stroke-width="1.2"/></svg></span>
</div>

<h2 class="blog-title">Latest Blog Articles</h2>
<section class="posts">
  <article class="post">
    <div class="post-photo" role="img" aria-label="Two friends smiling outdoors" style="background:linear-gradient(160deg,#a7b98a,#c9a17f)"></div>
    <h4>Blog Post Title Here</h4><time>30 December 2014</time>
    <p>Short stories of people doing good things in their communities every day.</p>
    <span class="more">Read More</span>
  </article>
  <article class="post">
    <div class="post-photo" role="img" aria-label="Man in a suit gesturing" style="background:linear-gradient(160deg,#e6e8ec,#9aa3b2)"></div>
    <h4>Blog Post Title Here</h4><time>30 December 2014</time>
    <p>How volunteers use the app to organise events and meet new helpers.</p>
    <span class="more">Read More</span>
  </article>
  <article class="post">
    <div class="post-photo" role="img" aria-label="Businessman talking on a phone" style="background:linear-gradient(160deg,#eceff3,#7f8a9b)"></div>
    <h4>Blog Post Title Here</h4><time>30 December 2014</time>
    <p>Tips for students and parents sharing small acts of kindness with friends.</p>
    <span class="more">Read More</span>
  </article>
  <article class="post">
    <div class="post-photo" role="img" aria-label="Hand holding a smartphone" style="background:linear-gradient(160deg,#6f9fc6,#d8dfe6)"></div>
    <h4>Blog Post Title Here</h4><time>30 December 2014</time>
    <p>News from our team on features that make giving back simple and fun.</p>
    <span class="more">Read More</span>
  </article>
</section>

<section class="newsletter">
  <h2><svg width="22" height="16" viewBox="0 0 22 16"><rect width="22" height="16" rx="2" fill="#555"/><path d="M1 2l10 7 10-7" fill="none" stroke="#f1f1f1" stroke-width="1.5"/></svg>Subscribe our Newsletter</h2>
  <div class="signup"><div class="field">your email address</div><div class="submit">SUBMIT</div></div>
</section>

<footer class="footer">
  <h5>Say Hi, Get In Touch</h5>
  <div class="socials"><span></span><span></span><span></span><span></span><span></span><span></span></div>
  <div class="legal">© 2014 Vok. All Rights Reserved · Contact · Press · Support · Developers · Privacy</div>
</footer>

</body>
</html>
```